Wordpress Contest Brief I would like a WordPress theme designed

Industry / Entity Type

Financial consultancy / advisers

Current site is: http://www.quorvel-group.com

Looking for a complete overhaul of this site, we are after a clean modern look. Will require the ability to easily add, update and remove content, hence the WordPress design.
Example:
Add case studies
Industry documentation (downloadable brochures / flyers and such)

What we like from our current site is the colour the fonts and the logo (the city of London) we would like to have other city outlines (NYC and Tokyo, Hong Kong, Singapore).

The site will be used by our potential clients to get in contact and re-view the case studies, if possible would like to have a client login area where they can download our documents like NDA’s etc and T&C’s.

Task Outline

Create a Web Design (Coded - Design and coding required)
Designer must provide full implementation/coding depending on the platform chosen by the client (i.e. WordPress theme, HTML/CSS, bootstrap etc.)

Task Description

I need a full website built that must work on desktop and mobile. I can provide the London city skyline and the font file, which we have used. Some stock industrial photos will be required.

Requirements:

*Splash page
*What We Do
*How We do it
*Who Are We? To have the same information and links as the current site
*Why use us?
*Clients: To have the same information and links as the current site
*Partners: To have the same information and links as the current site
*Contact:

Target Market(s)

Financial institutions trading Equities, Futures, Options, Forex and Fixed Income.
Regulators, Exchanges, ECN’s
Buy side firms and Sell side firms

Industry/Entity Type

Financial

Coding

Coded - Design and coding required

Number of Pages Required

5+ page

Font styles to use
Sans Serif

Colors
f04a50

Requirements
Must have
• Splash page
• What We Do
• How We do it
• Who Are We? To have the same information and links as the current site
• Why use us?
• Clients: To have the same information and links as the current site
• Partners: To have the same information and links as the current site
• Contact:

```html
<!DOCTYPE html>
<html lang="en">
<head>
<meta charset="utf-8">
<title>Quorvel Advisers</title>
<link href="https://fonts.googleapis.com/css2?family=Open+Sans:wght@400;600;700&family=Raleway:wght@300;400;500&display=swap" rel="stylesheet">
<style>
:root{
  --red:#f04a50;
  --ink:#2b2b2b;
  --muted:#777;
  --line:#dcdcdc;
  --panel:#f4f4f4;
  --white:#fff;
  --navy:#1a2a44;
  --icon:#8a8a8a;
}
*{box-sizing:border-box;margin:0;padding:0}
html,body{width:1200px;height:3169px;overflow:hidden}
body{position:relative;background:var(--white);font-family:"Open Sans",Arial,sans-serif;color:var(--ink)}
.abs{position:absolute}
.heading{font-family:"Raleway",Arial,sans-serif;font-weight:500;font-variant:small-caps;letter-spacing:1px;font-size:34px;line-height:40px;color:var(--ink)}
.btn{position:absolute;border:1.5px solid var(--red);border-radius:20px;color:var(--red);font-size:12px;font-weight:600;letter-spacing:.5px;display:flex;align-items:center;justify-content:center;text-transform:uppercase;background:var(--white)}

/* hero */
.hero{position:absolute;left:0;top:0;width:1200px;height:550px;background:linear-gradient(180deg,#0e1c33 0%,#2c3e5c 35%,#4a4438 62%,#a9733c 78%,#1e1a1c 100%)}
.logo{position:absolute;left:95px;top:30px;display:flex;align-items:center;gap:10px;color:var(--white);font-size:17px;font-weight:600;letter-spacing:1px}
.logo-mark{width:14px;height:14px;border:1.5px solid currentColor}
.nav{position:absolute;top:40px;right:95px;display:flex;gap:22px;font-size:14px;color:var(--white)}
.nav .active{color:var(--red)}
.hero-title{position:absolute;top:196px;width:100%;text-align:center;font-family:"Raleway",Arial,sans-serif;font-weight:400;font-size:42px;letter-spacing:2px;color:var(--white)}
.hero-sub{position:absolute;top:262px;width:100%;text-align:center;font-size:19px;line-height:34px;color:var(--white);letter-spacing:.5px}
.hero-btn{position:absolute;left:488px;top:356px;width:225px;height:42px;border-radius:21px;background:var(--red);color:var(--white);font-size:15px;font-weight:600;display:flex;align-items:center;justify-content:center}
.dots{position:absolute;top:480px;left:564px;display:flex;gap:6px}
.dots span{width:13px;height:13px;border-radius:50%;border:2px solid var(--white)}
.dots span:first-child{background:var(--white)}

/* what we do */
.service{position:absolute;top:706px;width:260px;text-align:center}
.service-title{margin-top:22px;font-family:"Raleway",Arial,sans-serif;font-variant:small-caps;font-size:18px;font-weight:500;letter-spacing:.5px}
.service-text{margin-top:8px;font-size:12px;line-height:19px;color:#555}

/* how */
.how{position:absolute;left:0;top:1015px;width:1200px;height:413px;background:var(--panel)}
.body-text{font-size:12.5px;line-height:23px;color:#666}

/* why */
.ticks{list-style:none}
.ticks li{display:flex;align-items:center;gap:14px;height:38px;font-size:12.5px;color:#555}

/* team */
.team{position:absolute;left:0;top:1878px;width:1200px;height:424px;background:var(--panel)}
.member{position:absolute;top:110px;width:240px;text-align:center}
.member-photo{width:186px;height:186px;margin:0 auto;border-radius:50%;border:5px solid var(--white);box-shadow:0 0 0 1px #ddd;background:radial-gradient(circle at 50% 40%,#c9b7a6,#7d8a97)}
.member-name{margin-top:22px;font-family:"Raleway",Arial,sans-serif;font-variant:small-caps;font-size:19px;letter-spacing:.5px}
.member-role{margin-top:3px;font-size:13px;color:var(--red)}

/* partners / clients */
.tile{position:absolute;width:222px;height:87px;background:var(--white);border:2px solid #e6e6e6;display:flex;align-items:center;justify-content:center;gap:8px;font-size:17px;font-weight:700;color:var(--navy)}
.tile.small{width:201px;height:77px;border:1px solid #e0e0e0}
.tile i{width:12px;height:12px;border-radius:50%;background:var(--red)}
.clients-panel{position:absolute;left:637px;top:2437px;width:467px;height:309px;background:#e9e9e9;border:1px solid #ddd}
.arrow{position:absolute;width:34px;height:34px;border-radius:50%;background:var(--white);border:1px solid #ccc;display:flex;align-items:center;justify-content:center}

/* footer */
.footer{position:absolute;left:0;top:2814px;width:1200px;height:355px;border-top:3px solid var(--red)}
.footer-heading{font-family:"Raleway",Arial,sans-serif;font-variant:small-caps;font-size:17px;letter-spacing:1px;color:var(--ink)}
.footer-links{list-style:none;margin-top:14px;font-size:12px;line-height:19.6px;color:#555}
.footer-text{font-size:12px;line-height:20px;color:#555}
.contact-row{display:flex;gap:14px;font-size:12px;line-height:22px;color:#555}
.social{position:absolute;left:990px;top:3120px;display:flex;gap:6px}
.social span{width:24px;height:24px;border-radius:50%;border:1px solid var(--red)}
</style>
</head>
<body>

<header class="hero" role="img" aria-label="Night photograph of a city river bridge with lit buildings reflected in the water">
  <div class="logo"><span class="logo-mark"></span>QUORVEL ADVISERS</div>
  <nav class="nav">
    <span class="active">Home</span><span>What we do</span><span>How we do it</span><span>Who are we</span><span>Why use us</span><span>Clients</span><span>Partners</span><span>Contact</span>
    <svg width="14" height="14" viewBox="0 0 14 14"><circle cx="6" cy="6" r="4.5" fill="none" stroke="#fff" stroke-width="2"/><line x1="9.5" y1="9.5" x2="13" y2="13" stroke="#fff" stroke-width="2"/></svg>
  </nav>
  <h1 class="hero-title">QUORVEL ADVISERS</h1>
  <p class="hero-sub">Provide solutions to solve potential issues to get you the correct solution<br>at the correct price point to achieve the desired results</p>
  <div class="hero-btn">GET MORE INFO &gt;&gt;</div>
  <div class="dots"><span></span><span></span><span></span><span></span></div>
</header>

<section class="what">
  <h2 class="heading abs" style="top:612px;width:1200px;text-align:center">What We Do</h2>

  <div class="service" style="left:60px">
    <svg width="140" height="140" viewBox="0 0 140 140" role="img" aria-label="Advice icon">
      <circle cx="70" cy="70" r="66" fill="#fff" stroke="#ccc" stroke-width="4"/><circle cx="70" cy="70" r="56" fill="#e4e4e4"/>
      <g fill="none" stroke="#8a8a8a" stroke-width="3" stroke-linecap="round">
        <path d="M58 82 C50 76 48 70 48 64 A22 22 0 0 1 92 64 C92 70 90 76 82 82 L82 88 L58 88 Z" fill="#8a8a8a" stroke="none"/>
        <line x1="60" y1="94" x2="80" y2="94"/><line x1="63" y1="100" x2="77" y2="100"/>
        <line x1="70" y1="30" x2="70" y2="36"/><line x1="44" y1="40" x2="48" y2="44"/><line x1="96" y1="40" x2="92" y2="44"/>
        <line x1="36" y1="64" x2="42" y2="64"/><line x1="98" y1="64" x2="104" y2="64"/>
      </g>
      <text x="70" y="74" text-anchor="middle" font-family="Open Sans, Arial, sans-serif" font-size="22" font-weight="700" fill="#e4e4e4">$</text>
    </svg>
    <div class="service-title">Advice</div>
    <div class="service-text">Board Level Advisory<br>&amp; Programme Management</div>
  </div>

  <div class="service" style="left:321px">
    <svg width="140" height="140" viewBox="0 0 140 140" role="img" aria-label="Product development icon">
      <circle cx="70" cy="70" r="66" fill="#fff" stroke="#ccc" stroke-width="4"/><circle cx="70" cy="70" r="56" fill="#e4e4e4"/>
      <g fill="#8a8a8a">
        <circle cx="52" cy="46" r="7"/><circle cx="70" cy="42" r="8"/><circle cx="88" cy="46" r="7"/>
        <path d="M40 68 C40 58 64 58 64 68 Z"/><path d="M57 66 C57 52 83 52 83 66 Z"/><path d="M76 68 C76 58 100 58 100 68 Z"/>
      </g>
      <g fill="none" stroke="#8a8a8a">
        <circle cx="52" cy="88" r="9" stroke-width="4"/><circle cx="52" cy="88" r="13" stroke-width="5" stroke-dasharray="4 3.3"/>
        <circle cx="70" cy="86" r="7" stroke-width="4"/><circle cx="70" cy="86" r="10" stroke-width="4" stroke-dasharray="3.5 2.8"/>
        <circle cx="88" cy="88" r="9" stroke-width="4"/><circle cx="88" cy="88" r="13" stroke-width="5" stroke-dasharray="4 3.3"/>
      </g>
    </svg>
    <div class="service-title">Product Developement</div>
    <div class="service-text">Front-office Trading Platforms &amp;<br>Market Data Pre | At | Post Trade Risk</div>
  </div>

  <div class="service" style="left:583px">
    <svg width="140" height="160" viewBox="0 0 140 160" role="img" aria-label="Interim management icon" style="margin-bottom:-20px">
      <path d="M70 152 L52 130 A66 66 0 1 1 88 130 Z" fill="#fff" stroke="#ccc" stroke-width="4"/><circle cx="70" cy="70" r="56" fill="#f04a50"/>
      <g fill="#fff">
        <circle cx="70" cy="38" r="7"/><path d="M58 56 C58 44 82 44 82 56 Z"/>
        <rect x="36" y="84" width="18" height="14"/><rect x="61" y="84" width="18" height="14"/><rect x="86" y="84" width="18" height="14"/>
      </g>
      <g fill="none" stroke="#fff" stroke-width="2.5">
        <line x1="70" y1="58" x2="70" y2="84"/><path d="M45 84 L45 72 L95 72 L95 84"/>
      </g>
    </svg>
    <div class="service-title">Interim Management</div>
    <div class="service-text">For Funds, Brockers, Vendors<br>and IT Services providers</div>
  </div>

  <div class="service" style="left:843px">
    <svg width="140" height="140" viewBox="0 0 140 140" role="img" aria-label="Process outsourcing icon">
      <circle cx="70" cy="70" r="66" fill="#fff" stroke="#ccc" stroke-width="4"/><circle cx="70" cy="70" r="56" fill="#e4e4e4"/>
      <g fill="none" stroke="#8a8a8a" stroke-width="4">
        <path d="M42 60 A30 30 0 0 1 94 50"/><path d="M98 80 A30 30 0 0 1 46 90"/>
      </g>
      <g fill="#8a8a8a">
        <path d="M90 40 L102 52 L88 56 Z"/><path d="M50 100 L38 88 L52 84 Z"/>
        <circle cx="58" cy="64" r="5"/><circle cx="70" cy="62" r="5"/><circle cx="82" cy="64" r="5"/>
        <path d="M50 80 C50 70 66 70 66 80 Z"/><path d="M62 78 C62 68 78 68 78 78 Z"/><path d="M74 80 C74 70 90 70 90 80 Z"/>
      </g>
    </svg>
    <div class="service-title">Process Outsourcing</div>
    <div class="service-text">RFI, RFP &amp; Independent tender<br>evaluations (assess befor you invest)</div>
  </div>
</section>

<section class="how">
  <svg class="abs" style="left:0;top:0" width="624" height="413" viewBox="0 0 624 413" role="img" aria-label="Glowing light bulb with gears on a dark chalkboard background">
    <defs><radialGradient id="bulbGlow" cx="30%" cy="40%" r="70%"><stop offset="0" stop-color="#c9a86a"/><stop offset=".35" stop-color="#5d5a52"/><stop offset="1" stop-color="#2a2e35"/></radialGradient></defs>
    <polygon points="0,0 624,0 518,413 0,413" fill="url(#bulbGlow)"/>
  </svg>
  <h2 class="heading abs" style="left:666px;top:62px">How We Do It</h2>
  <p class="body-text abs" style="left:666px;top:116px;width:450px">At vero eos et accusamus et iusto odio dignissimos ducimus qui blanditiis praesent ium voluptatum deleniti atque corrupti quo.</p>
  <p class="body-text abs" style="left:666px;top:192px;width:450px">Dolores et quas molestias excepturi sint occaecati cupiditate non provident similiq ue sunt in culpa qui officia deserunt mollitia animi, id est laborum et dolorum fug t harum quidem rerum facilis est et expedita voluptas assumen est, omnis dolorr epellend poribus autem quibusdam et aut officiis.</p>
  <div class="btn" style="left:666px;top:313px;width:132px;height:32px">Read more &gt;&gt;</div>
</section>

<section class="why">
  <h2 class="heading abs" style="left:100px;top:1500px">Why Choose us</h2>
  <ul class="ticks abs" style="left:100px;top:1559px">
    <li><svg width="14" height="14" viewBox="0 0 14 14"><circle cx="7" cy="7" r="7" fill="#f04a50"/><path d="M3.8 7.2 L6 9.3 L10.2 4.9" fill="none" stroke="#fff" stroke-width="1.8"/></svg>At vero eos et accusamus et iusto odio dignissimos ducimus qui blanis</li>
    <li><svg width="14" height="14" viewBox="0 0 14 14"><circle cx="7" cy="7" r="7" fill="#f04a50"/><path d="M3.8 7.2 L6 9.3 L10.2 4.9" fill="none" stroke="#fff" stroke-width="1.8"/></svg>Praesentium voluptatum deleniti atque corrupti quos dolores et quas</li>
    <li><svg width="14" height="14" viewBox="0 0 14 14"><circle cx="7" cy="7" r="7" fill="#f04a50"/><path d="M3.8 7.2 L6 9.3 L10.2 4.9" fill="none" stroke="#fff" stroke-width="1.8"/></svg>Excepturi sint occaecati cupiditate non provident, similiqt in culpa qui</li>
    <li><svg width="14" height="14" viewBox="0 0 14 14"><circle cx="7" cy="7" r="7" fill="#f04a50"/><path d="M3.8 7.2 L6 9.3 L10.2 4.9" fill="none" stroke="#fff" stroke-width="1.8"/></svg>Nam litero tempore, cum soluta nobis est eligendi optio</li>
    <li><svg width="14" height="14" viewBox="0 0 14 14"><circle cx="7" cy="7" r="7" fill="#f04a50"/><path d="M3.8 7.2 L6 9.3 L10.2 4.9" fill="none" stroke="#fff" stroke-width="1.8"/></svg>Dil quo minus id quod maxime placeat facere possimus, omnis volup</li>
  </ul>
  <div class="btn" style="left:100px;top:1771px;width:145px;height:33px">Read more &gt;&gt;</div>

  <svg class="abs" style="left:630px;top:1502px" width="523" height="307" viewBox="0 0 523 307" role="img" aria-label="Laptop screen showing a trading price line chart">
    <rect x="40" y="0" width="443" height="285" rx="10" fill="#1b1d21"/>
    <rect x="52" y="12" width="419" height="261" fill="#f7f7f9"/>
    <rect x="52" y="12" width="419" height="14" fill="#d9dde3"/>
    <g stroke="#e3e5ea" stroke-width="1">
      <line x1="60" y1="60" x2="462" y2="60"/><line x1="60" y1="100" x2="462" y2="100"/><line x1="60" y1="140" x2="462" y2="140"/><line x1="60" y1="180" x2="462" y2="180"/><line x1="60" y1="220" x2="462" y2="220"/>
      <line x1="140" y1="34" x2="140" y2="250"/><line x1="220" y1="34" x2="220" y2="250"/><line x1="300" y1="34" x2="300" y2="250"/><line x1="380" y1="34" x2="380" y2="250"/>
    </g>
    <polyline fill="none" stroke="#2b4aa8" stroke-width="2" points="62,190 78,170 92,176 104,120 112,70 122,110 134,150 146,140 160,120 172,156 186,170 200,150 214,172 228,190 242,180 256,160 270,176 284,150 298,180 312,196 326,170 340,160 354,176 368,150 382,112 396,130 410,160 424,140 438,170 450,200 460,230"/>
    <polyline fill="none" stroke="#f04a50" stroke-width="1.5" points="62,198 90,184 120,150 150,156 180,168 210,170 240,182 270,172 300,184 330,178 360,166 390,140 420,156 450,188 460,210"/>
    <rect x="60" y="250" width="402" height="1" fill="#b9bdc4"/>
    <path d="M0 285 L523 285 L510 300 Q508 307 500 307 L23 307 Q15 307 13 300 Z" fill="#c9ccd1"/>
    <rect x="222" y="285" width="80" height="5" rx="2" fill="#a9adb3"/>
  </svg>
</section>

<section class="team">
  <h2 class="heading abs" style="top:42px;width:1200px;text-align:center">Who Are We</h2>
  <div class="member" style="left:70px"><div class="member-photo" role="img" aria-label="Portrait photo of Owen Hartley"></div><div class="member-name">Owen Hartley</div><div class="member-role">Director</div></div>
  <div class="member" style="left:345px"><div class="member-photo" role="img" aria-label="Portrait photo of Simon Ashcroft"></div><div class="member-name">Simon Ashcroft</div><div class="member-role">Director</div></div>
  <div class="member" style="left:618px"><div class="member-photo" role="img" aria-label="Portrait photo of Neil Brampton"></div><div class="member-name">Neil Brampton</div><div class="member-role">New Business Director</div></div>
  <div class="member" style="left:889px"><div class="member-photo" role="img" aria-label="Portrait photo of Helena Marsh"></div><div class="member-name">Helena Marsh</div><div class="member-role">Non-Executive Director</div></div>
</section>

<section class="partners">
  <h2 class="heading abs" style="left:100px;top:2368px">Our Partners</h2>
  <div class="tile" style="left:100px;top:2439px"><i></i>Tradeloop</div>
  <div class="tile" style="left:341px;top:2439px">Meridane Group</div>
  <div class="tile" style="left:100px;top:2547px"><i></i>Corvanta</div>
  <div class="tile" style="left:341px;top:2547px">Latencia</div>
  <div class="tile" style="left:100px;top:2655px"><i></i>Brightspan</div>
  <div class="tile" style="left:341px;top:2655px">Northwire Network</div>
</section>

<section class="clients">
  <h2 class="heading abs" style="left:637px;top:2368px">Our Clients</h2>
  <div class="clients-panel"></div>
  <div class="tile small" style="left:662px;top:2458px">Oltrix</div>
  <div class="tile small" style="left:878px;top:2458px">Meridane Group</div>
  <div class="tile small" style="left:662px;top:2555px">Cellora Memory</div>
  <div class="tile small" style="left:878px;top:2555px">Portway Lab</div>
  <div class="tile small" style="left:662px;top:2651px"><i></i>Tradeloop</div>
  <div class="tile small" style="left:878px;top:2651px">Tidemark Capital</div>
  <div class="arrow" style="left:637px;top:2575px"><svg width="10" height="14" viewBox="0 0 10 14"><path d="M8 1 L2 7 L8 13" fill="none" stroke="#555" stroke-width="2"/></svg></div>
  <div class="arrow" style="left:1066px;top:2575px"><svg width="10" height="14" viewBox="0 0 10 14"><path d="M2 1 L8 7 L2 13" fill="none" stroke="#555" stroke-width="2"/></svg></div>
</section>

<footer class="footer">
  <div class="abs" style="left:100px;top:122px;display:flex;align-items:center;gap:10px;font-size:17px;font-weight:600;letter-spacing:1px;color:var(--ink)"><span style="width:14px;height:14px;border:1.5px solid var(--ink)"></span>QUORVEL ADVISERS</div>

  <div class="abs" style="left:400px;top:56px">
    <div class="footer-heading">Information</div>
    <ul class="footer-links"><li>Home</li><li>What we do</li><li>How we do it</li><li>Who are we</li><li>Why use us</li><li>Clients</li><li>Partners</li><li>Contact</li></ul>
  </div>

  <div class="abs" style="left:592px;top:56px;width:260px">
    <div class="footer-heading">Newsletter Subscription</div>
    <p class="footer-text" style="margin-top:14px">Register your Email Address to get<br>Information about us</p>
    <div style="margin-top:18px;font-size:11px;color:#999;padding-bottom:6px;border-bottom:1px solid var(--line)">Email Address</div>
    <div class="btn" style="position:relative;margin-top:20px;width:94px;height:30px;font-size:11px">Subscribe</div>
  </div>

  <div class="abs" style="left:916px;top:56px;width:200px">
    <div class="footer-heading">Contact Us</div>
    <div class="contact-row" style="margin-top:14px"><svg width="12" height="16" viewBox="0 0 12 16" style="margin-top:4px;flex:none"><path d="M6 0 A6 6 0 0 1 12 6 C12 10 6 16 6 16 C6 16 0 10 0 6 A6 6 0 0 1 6 0 Z" fill="#f04a50"/><circle cx="6" cy="6" r="2.2" fill="#fff"/></svg><span>Suite 4 Alder Court,<br>Brookfield, Westbury,<br>Hants, WB12 4QP</span></div>
    <div class="contact-row" style="margin-top:12px"><svg width="12" height="12" viewBox="0 0 12 12" style="margin-top:5px;flex:none"><path d="M2 0 L4.5 0 L5.5 3 L4 4.5 C4.8 6 6 7.2 7.5 8 L9 6.5 L12 7.5 L12 10 C12 11 11 12 10 12 C4.5 12 0 7.5 0 2 C0 1 1 0 2 0 Z" fill="#f04a50"/></svg><span>+1-555-010-2040</span></div>
    <div class="contact-row" style="margin-top:20px"><svg width="12" height="10" viewBox="0 0 12 10" style="margin-top:6px;flex:none"><rect width="12" height="10" fill="#f04a50"/><path d="M0 0 L6 5 L12 0" fill="none" stroke="#fff" stroke-width="1.2"/></svg><span>info@quorvel-group.com</span></div>
  </div>

  <div class="abs" style="left:100px;top:272px;width:1000px;border-top:1px solid var(--line)"></div>
  <p class="abs footer-text" style="left:100px;top:308px">Copyrights © 2017, Quorvel Advisers. All rights reserved.</p>
</footer>
<div class="social"><span></span><span></span><span></span><span></span></div>

</body>
</html>
```